TK Joinery

Cabinet maker. Kitchens. Wardrobes. Vanitys. Entertainment units

Target Market(s)

Modern contemporary.geometry. colours black, gray, charcoal and orange. Matt card gloss letters

Industry/Entity Type

Entertainment

Contact Information for Business Card

Mattias Velder 0418 295 437
mattias.velder@fernmail.test
ABN 471 9052 8316

Font styles to use
Decorative

Colors
000000

Requirements
Should not have
• Pictures

```html
<!DOCTYPE html>
<html lang="en">
<head>
<meta charset="utf-8">
<title>Mattias Velder – Business Card</title>
<link rel="stylesheet" href="https://fonts.googleapis.com/css2?family=Lato:wght@400;700&family=Yellowtail&display=swap">
<style>
  :root {
    --backdrop: #e9e7e3;
    --card: #232323;
    --grey-text: #5e5e5e;
    --orange: #e2622b;
    --shadow: rgba(0, 0, 0, 0.22);
  }
  * { box-sizing: border-box; margin: 0; padding: 0; }
  html, body {
    width: 1200px;
    height: 926px;
    overflow: hidden;
    background: var(--backdrop);
  }
  .canvas {
    width: 1200px;
    height: 926px;
    display: flex;
    flex-direction: column;
    align-items: center;
    justify-content: center;
    gap: 46px;
  }
  .card {
    position: relative;
    width: 700px;
    height: 400px;
    background: var(--card);
    box-shadow: 0 10px 26px var(--shadow);
    font-family: "Lato", sans-serif;
  }
  .card-front__name {
    position: absolute;
    left: 64px;
    top: 54px;
    font-family: "Yellowtail", cursive;
    font-size: 58px;
    color: var(--grey-text);
    letter-spacing: 0.5px;
  }
  .card-front__abn {
    position: absolute;
    left: 64px;
    top: 254px;
    font-size: 20px;
    font-weight: 700;
    color: var(--orange);
  }
  .card-front__contact {
    position: absolute;
    right: 56px;
    bottom: 40px;
    text-align: right;
    color: var(--grey-text);
  }
  .card-front__phone {
    font-size: 31px;
    font-weight: 700;
    line-height: 1.15;
  }
  .card-front__email {
    font-size: 21px;
    font-weight: 400;
  }
  .card-back__services {
    position: absolute;
    left: 0;
    right: 0;
    top: 64px;
    text-align: center;
    font-size: 15px;
    letter-spacing: 1.6px;
    color: var(--orange);
  }
</style>
</head>
<body>
  <main class="canvas">
    <section class="card card-back" aria-label="Card back">
      <p class="card-back__services">Cabinet maker · Kitchens · Wardrobes · Vanitys · Entertainment units</p>
    </section>
    <section class="card card-front" aria-label="Card front">
      <h1 class="card-front__name">Mattias Velder</h1>
      <p class="card-front__abn">ABN 471 9052 8316</p>
      <div class="card-front__contact">
        <p class="card-front__phone">0418 295 437</p>
        <p class="card-front__email">mattias.velder@fernmail.test</p>
      </div>
    </section>
  </main>
</body>
</html>
```